Brightfold Partners Website

Brightfold Partners (BP) provide Analytics & Enterprise Performance Management (EPM) advisory & consultancy services. We are passionate about data and making a difference for our clients by working in partnership with them, helping them on their journey to becoming an Brightfold Partner. We deliver insights which give our clients a competitive edge and a much deeper understanding of their organisation.

We need a website which shows who we are, what we do and how we do it.

www.brightfold-partners.example is our very basic website at the moment. We want to completely revamp it with a corporate look

```html
<!DOCTYPE html>
<html lang="en">
<head>
<meta charset="utf-8">
<title>Brightfold Partners</title>
<link href="https://fonts.googleapis.com/css2?family=Montserrat:wght@500;600;700&family=Roboto:wght@400;500&display=swap" rel="stylesheet">
<style>
  :root {
    --brand: #2c5670;
    --brand-dark: #244a61;
    --white: #ffffff;
    --ink-soft: #dfe6ea;
  }
  * { box-sizing: border-box; margin: 0; padding: 0; }
  html, body { width: 1200px; height: 853px; overflow: hidden; background: var(--white); }
  body { position: relative; font-family: "Roboto", sans-serif; }

  .topbar {
    position: absolute; left: 0; top: 0; width: 1200px; height: 58px;
    background: var(--brand); color: var(--white);
    display: flex; align-items: center; justify-content: space-between;
    padding: 0 67px;
  }
  .topbar__info { display: flex; align-items: center; font-size: 15px; }
  .topbar__phone { display: flex; align-items: center; margin-left: 10px; font-family: "Montserrat", sans-serif; font-weight: 600; font-size: 15.5px; }
  .topbar__phone svg { margin-right: 9px; }
  .topbar__social { display: flex; align-items: center; gap: 22px; }
  .social-tile { width: 27px; height: 27px; background: var(--white); border-radius: 2px; }

  .header {
    position: absolute; left: 0; top: 58px; width: 1200px; height: 100px;
    background: var(--white);
    display: flex; align-items: center; justify-content: space-between;
    padding: 0 67px;
  }
  .brand { display: flex; align-items: center; gap: 14px; }
  .brand__mark { width: 60px; height: 60px; border-radius: 50%; background: var(--brand); }
  .brand__name {
    font-family: "Montserrat", sans-serif; font-weight: 700; font-size: 21px;
    line-height: 25px; color: var(--brand); text-transform: uppercase;
  }
  .nav { display: flex; gap: 50px; align-items: center; }
  .nav__link {
    position: relative; font-family: "Montserrat", sans-serif; font-weight: 500;
    font-size: 17px; color: var(--brand); text-transform: uppercase; text-decoration: none;
    display: flex; align-items: center; gap: 7px;
  }
  .nav__link--active { font-weight: 700; }
  .nav__link--active::after {
    content: ""; position: absolute; left: -2px; right: -2px; bottom: -10px;
    height: 4px; background: var(--brand);
  }

  .hero { position: absolute; left: 0; top: 158px; width: 1200px; height: 695px; overflow: hidden; }
  .hero__photo {
    position: absolute; inset: 0;
    background:
      linear-gradient(90deg, rgba(30,34,38,0.75) 0%, rgba(40,44,48,0.45) 45%, rgba(0,0,0,0) 80%),
      radial-gradient(ellipse at 85% 20%, #e9ecee 0%, #b9c0c5 35%, transparent 60%),
      radial-gradient(ellipse at 60% 70%, #1f2b3d 0%, #2a3442 40%, transparent 70%),
      linear-gradient(120deg, #4a4f54 0%, #6c7277 40%, #3b4047 70%, #9aa1a6 100%);
  }
  .hero__content { position: absolute; left: 67px; top: 0; color: var(--white); }
  .hero__title {
    position: absolute; top: 132px; left: 0; width: 700px;
    font-family: "Montserrat", sans-serif; font-weight: 700; font-size: 60px;
    line-height: 88px; letter-spacing: 1px; text-transform: uppercase;
  }
  .hero__tagline { position: absolute; top: 316px; left: 0; width: 800px; font-size: 33px; }
  .btn {
    position: absolute; top: 403px; left: 0; width: 217px; height: 67px;
    background: var(--brand); color: var(--white);
    font-family: "Montserrat", sans-serif; font-weight: 500; font-size: 23px;
    display: flex; align-items: center; justify-content: center; text-decoration: none;
  }
  .link-more {
    position: absolute; top: 418px; left: 262px; color: var(--white);
    font-family: "Montserrat", sans-serif; font-weight: 500; font-size: 23px;
    text-decoration: none; border-bottom: 2px solid var(--white); padding: 0 3px 2px 0;
  }
  .scroll-cue { position: absolute; left: 579px; top: 636px; }
</style>
</head>
<body>
  <div class="topbar">
    <div class="topbar__info">
      <span>For more information :</span>
      <span class="topbar__phone">
        <svg width="26" height="26" viewBox="0 0 24 24" fill="none" stroke="#fff" stroke-width="2" stroke-linecap="round">
          <path d="M5 3h4l2 5-2.5 1.5a11 11 0 0 0 6 6L16 13l5 2v4a2 2 0 0 1-2 2A16 16 0 0 1 3 5a2 2 0 0 1 2-2z" fill="#fff"/>
          <path d="M14 6a4 4 0 0 1 4 4M14 2a8 8 0 0 1 8 8"/>
        </svg>
        01 555 0142
      </span>
    </div>
    <div class="topbar__social">
      <span class="social-tile"></span>
      <span class="social-tile"></span>
      <span class="social-tile"></span>
      <svg width="34" height="27" viewBox="0 0 34 27" fill="none" stroke="#fff" stroke-width="2.5">
        <rect x="1.5" y="1.5" width="31" height="24"/>
        <path d="M1.5 1.5 17 15 32.5 1.5"/>
      </svg>
    </div>
  </div>

  <header class="header">
    <div class="brand">
      <span class="brand__mark"></span>
      <span class="brand__name">Brightfold<br>Partners</span>
    </div>
    <nav class="nav">
      <a class="nav__link nav__link--active" href="#">Home</a>
      <a class="nav__link" href="#">Services
        <svg width="14" height="10" viewBox="0 0 14 10" fill="none" stroke="#2c5670" stroke-width="2.5"><path d="M1.5 2 7 7.5 12.5 2"/></svg>
      </a>
      <a class="nav__link" href="#">About Us</a>
      <a class="nav__link" href="#">Contact Us</a>
    </nav>
  </header>

  <section class="hero">
    <div class="hero__photo" role="img" aria-label="Photo of two consultants in suits reviewing charts on a laptop in a bright office"></div>
    <div class="hero__content">
      <h1 class="hero__title">Brightfold<br>Partners</h1>
      <p class="hero__tagline">Data Analytics &amp; EPM Consulting services</p>
      <a class="btn" href="#">Contact Us</a>
      <a class="link-more" href="#">Learn More</a>
    </div>
    <svg class="scroll-cue" width="42" height="42" viewBox="0 0 42 42" fill="none" stroke="#fff" stroke-width="3">
      <circle cx="21" cy="21" r="19"/>
      <path d="M13 18l8 8 8-8" stroke-linecap="round"/>
    </svg>
  </section>
</body>
</html>
```